Business cards for a fleet management app
logo, web address, and see notes below
Business cards for a fleet management app - Transportation
Creative Brief
Use same font as used in my logo
Marlo Quennell
Director of Sales
NONE
dennis@harborvanledger.com
harborvanledger.com
No Back-end Portal Maintenance Files Driver Qualification Email Notifications Permit Tracking DVIR's
logo see attached and harborvanledger.com
guinnjoe guinnjoe
This should be printed on the card somewhere front or back No Back-end Portal Maintenance Files Driver Qualification Email Notifications Permit Tracking DVIR's

```html
<!DOCTYPE html>
<html lang="en">
<head>
<meta charset="utf-8">
<title>Harbor Van Ledger – Business Cards</title>
<link rel="stylesheet" href="https://fonts.googleapis.com/css2?family=Source+Sans+3:ital,wght@0,400;0,600;1,400&family=Tenor+Sans&display=swap">
<style>
  :root {
    --backdrop: #3b3b3b;
    --card-white: #f7f7f7;
    --brand-teal: #1789b5;
    --band-blue: #19a6d8;
    --band-blue-deep: #1390c0;
    --ink: #2e2e2e;
    --ink-soft: #444444;
    --white: #ffffff;
  }
  * { margin: 0; padding: 0; box-sizing: border-box; }
  html, body { width: 1200px; height: 751px; overflow: hidden; }
  body {
    background: var(--backdrop);
    font-family: "Source Sans 3", sans-serif;
    position: relative;
  }
  .card {
    position: absolute;
    top: 219px;
    width: 493px;
    height: 281px;
    background: var(--card-white);
    overflow: hidden;
  }
  .card--front { left: 91px; }
  .card--back { left: 620px; }

  /* Front */
  .brand-mark {
    position: absolute;
    left: 0; top: 27px;
    width: 62px; height: 62px;
    background: var(--brand-teal);
  }
  .brand-name {
    position: absolute;
    font-family: "Source Sans 3", sans-serif;
    font-weight: 600;
    color: var(--brand-teal);
    letter-spacing: 0.5px;
    white-space: nowrap;
  }
  .card--front .brand-name { left: 78px; top: 42px; font-size: 29px; }
  .person-name {
    position: absolute;
    left: 103px; top: 131px;
    font-family: "Tenor Sans", sans-serif;
    font-weight: 400;
    font-size: 21px;
    color: var(--brand-teal);
    white-space: nowrap;
  }
  .person-title {
    position: absolute;
    left: 103px; top: 157px;
    font-size: 15.5px;
    color: var(--ink);
  }
  .contact-list {
    position: absolute;
    left: 103px; top: 193px;
    list-style: none;
  }
  .contact-list li {
    display: flex;
    align-items: center;
    height: 20px;
    font-size: 14px;
    color: var(--ink-soft);
    white-space: nowrap;
  }
  .contact-list svg { width: 11px; height: 11px; margin-right: 9px; flex: none; }

  /* Back */
  .card--back .brand-name { left: 28px; top: 20px; font-size: 32px; }
  .web-line {
    position: absolute;
    left: 29px; top: 76px;
    font-style: italic;
    font-size: 13.5px;
    letter-spacing: 3px;
    color: var(--ink);
  }
  .feature-band {
    position: absolute;
    left: 0; top: 107px;
    width: 100%; height: 174px;
    background: var(--band-blue);
  }
  .feature-band__shade {
    position: absolute;
    right: 0; top: 0;
    width: 108px; height: 100%;
    background: var(--band-blue-deep);
  }
  .feature-list {
    position: absolute;
    left: 30px; top: 31px;
    list-style: none;
    color: var(--white);
    font-size: 13.5px;
  }
  .feature-list li { height: 19.7px; line-height: 19.7px; }
  .feature-list li::before { content: "•"; margin-right: 8px; }
</style>
</head>
<body>
  <section class="card card--front">
    <div class="brand-mark"></div>
    <div class="brand-name">HARBOR VAN LEDGER</div>
    <h1 class="person-name">Marlo Quennell</h1>
    <p class="person-title">Director of Sales</p>
    <ul class="contact-list">
      <li>
        <svg viewBox="0 0 11 11" aria-hidden="true"><rect x="2.5" y="0.5" width="6" height="10" rx="1" fill="none" stroke="#1789b5" stroke-width="1.2"/><circle cx="5.5" cy="8.7" r="0.7" fill="#1789b5"/></svg>
        555.014.2273
      </li>
      <li>
        <svg viewBox="0 0 11 11" aria-hidden="true"><rect x="0.5" y="2" width="10" height="7" fill="#1789b5"/><path d="M0.5 2 L5.5 6 L10.5 2" fill="none" stroke="#f7f7f7" stroke-width="1"/></svg>
        dennis@harborvanledger.com
      </li>
      <li>
        <svg viewBox="0 0 11 11" aria-hidden="true"><circle cx="5.5" cy="5.5" r="4.7" fill="none" stroke="#1789b5" stroke-width="1"/><ellipse cx="5.5" cy="5.5" rx="2" ry="4.7" fill="none" stroke="#1789b5" stroke-width="0.8"/><line x1="0.8" y1="5.5" x2="10.2" y2="5.5" stroke="#1789b5" stroke-width="0.8"/></svg>
        harborvanledger.com
      </li>
    </ul>
  </section>

  <section class="card card--back">
    <div class="brand-name">HARBOR VAN LEDGER</div>
    <p class="web-line">harborvanledger.com</p>
    <div class="feature-band">
      <div class="feature-band__shade"></div>
      <ul class="feature-list">
        <li>No Back-end Portal</li>
        <li>Maintenance Files</li>
        <li>Driver Qualification</li>
        <li>Email Notifications</li>
        <li>Permit Tracking</li>
        <li>DVIR's</li>
      </ul>
    </div>
  </section>
</body>
</html>
```